Redesign for Popular UK Town Website

We're looking for someone to redesign a website for a popular tourist town that's visited by over 250,000 people a year. We have a basic design frame in place and need someone to make it look more 'professional.'
We've created a temporary design layout to show you a general idea of what we're looking for: http://quillhaven.co.uk/
All text/images are placeholder images so you can get an idea of the general layout.
(Please note that you can grab any images found on the internet for 'tenby' to be used as placeholder images. This is because we will be visiting the locations and taking our own photos, after the design is complete.)
Target Market(s)
Tourists
Industry/Entity Type
Town
Number of Pages Required
2 page
Requirements
Must have
- You need to redesign the homepage: http://quillhaven.co.uk/
- You also need to redesign the following page: http://quillhaven.co.uk/hotels/ (This page will be used for multiple categories and is used to list locations of properties/places etc.)
- Design must be responsive also.
Nice to have
- Please feel free to add as much as you can to the content/features as with our limited knowledge of websites, have only been able to create a basic layout.

```html
<!DOCTYPE html>
<html lang="en">
<head>
<meta charset="utf-8">
<title>Quillhaven – Visit the Town</title>
<link rel="stylesheet" href="https://fonts.googleapis.com/css2?family=Lato:ital,wght@0,400;0,700;0,900;1,400&display=swap">
<style>
  :root {
    --navy: #1c2d5e;
    --navy-band: rgba(24, 40, 92, 0.88);
    --white: #ffffff;
    --label-fill: rgba(128, 118, 70, 0.72);
    --label-border: rgba(230, 226, 205, 0.75);
    --news-bg: #1d2a30;
    --text-dark: #1a1a1a;
  }
  * { box-sizing: border-box; margin: 0; padding: 0; }
  html, body { width: 1200px; height: 1157px; overflow: hidden; }
  body { font-family: "Lato", sans-serif; color: var(--white); position: relative; background: var(--news-bg); }

  .hero {
    position: absolute; left: 0; top: 0; width: 1200px; height: 823px;
    background: linear-gradient(180deg, #45578a 0%, #6c7fa6 18%, #5b6a63 40%, #8a6a45 58%, #9b7448 72%, #355a63 88%, #2c4f5a 100%);
  }
  .news-backdrop {
    position: absolute; left: 0; top: 823px; width: 1200px; height: 334px;
    background: linear-gradient(160deg, #37453f 0%, #1f2e33 45%, #1a2b38 100%);
  }

  .site-header {
    position: absolute; left: 0; top: 0; width: 1200px; height: 125px;
    background: var(--navy-band); z-index: 3;
  }
  .brand {
    position: absolute; left: 62px; top: 48px;
    display: flex; align-items: center; gap: 8px;
    font-weight: 900; font-size: 18px; color: var(--white); letter-spacing: 0.5px;
  }
  .brand-dot { width: 14px; height: 14px; border-radius: 50%; background: var(--white); }
  .main-nav {
    position: absolute; left: 216px; top: 59px;
    display: flex; gap: 10px; font-weight: 700; font-size: 13.5px; letter-spacing: -0.2px;
    white-space: nowrap;
  }
  .phone-btn {
    position: absolute; left: 907px; top: 51px; width: 151px; height: 33px;
    background: var(--white); color: var(--text-dark); border-radius: 7px;
    display: flex; align-items: center; justify-content: center; gap: 7px;
    font-weight: 700; font-size: 13.5px;
  }

  .tile-photo { position: absolute; width: 344px; height: 231px; z-index: 1; }
  .tile-label {
    position: absolute; width: 316px; height: 71px;
    background: var(--label-fill); border: 2px solid var(--label-border);
    display: flex; align-items: center; justify-content: center;
    font-size: 28px; font-weight: 400; color: var(--white); white-space: nowrap;
  }

  .news-heading { position: absolute; top: 884px; left: 0; width: 1200px; text-align: center; }
  .news-heading h2 { font-weight: 900; font-size: 28px; letter-spacing: -0.3px; }
  .news-heading p { font-style: italic; font-size: 12px; margin-top: 4px; }
  .news-card { position: absolute; top: 992px; height: 165px; }
</style>
</head>
<body>
  <div class="hero" role="img" aria-label="Aerial photograph of the town beach, cliffs and sea"></div>
  <div class="news-backdrop" role="img" aria-label="Dimmed aerial photograph of the harbour"></div>

  <header class="site-header">
    <div class="brand"><span class="brand-dot"></span>Quillhaven</div>
    <nav class="main-nav">
      <span>WHERE TO STAY</span>
      <span>CARAVANS AND CAMPING</span>
      <span>BED AND BREAKFAST</span>
      <span>HOTELS IN QUILLHAVEN</span>
      <span>CONTACT</span>
    </nav>
    <div class="phone-btn">
      <svg width="11" height="11" viewBox="0 0 24 24" aria-hidden="true"><path fill="#1a1a1a" d="M6.6 10.8a15.1 15.1 0 0 0 6.6 6.6l2.2-2.2c.3-.3.7-.4 1-.2 1.1.4 2.3.6 3.6.6.6 0 1 .4 1 1V20c0 .6-.4 1-1 1A17 17 0 0 1 3 4c0-.6.4-1 1-1h3.5c.6 0 1 .4 1 1 0 1.3.2 2.5.6 3.6.1.3 0 .7-.2 1z"/></svg>
      44-1632-960-418
    </div>
  </header>

  <div class="tile-photo" style="left:34px;top:56px;background:linear-gradient(180deg,#3b4a8e,#9d7fbf 45%,#e6d3e6 75%,#6d7a88)" role="img" aria-label="Sunset sky over the colourful seafront"></div>
  <div class="tile-photo" style="left:430px;top:56px;background:linear-gradient(180deg,#3f5fa8,#8ea56a 40%,#d9cf9a 60%,#2f4a8a)" role="img" aria-label="Harbour with pastel houses and boats"></div>
  <div class="tile-photo" style="left:823px;top:56px;width:342px;background:linear-gradient(160deg,#58726a,#3cbfb3 50%,#1f8c96)" role="img" aria-label="Aerial view of an island and turquoise sea"></div>

  <div class="tile-label" style="left:46px;top:309px">Top 10 Beaches</div>
  <div class="tile-label" style="left:444px;top:309px">Top 5 Night-Clubs</div>
  <div class="tile-label" style="left:841px;top:309px">Top Hotels</div>

  <div class="tile-photo" style="left:34px;top:417px;background:linear-gradient(180deg,#dcdcdc,#8c8c8c 55%,#3a3a3a)" role="img" aria-label="Black and white hotel entrance"></div>
  <div class="tile-photo" style="left:430px;top:417px;background:linear-gradient(180deg,#3c63c8,#7f8fdc 45%,#c79aa8 55%,#2c3a8c)" role="img" aria-label="Castle reflected in a calm estuary"></div>
  <div class="tile-photo" style="left:823px;top:416px;width:342px;background:linear-gradient(180deg,#1d2f96,#8c95d8 40%,#e7e3f0 70%,#9b8e9a)" role="img" aria-label="Town skyline under a blue sky"></div>

  <div class="tile-label" style="left:46px;top:673px">Top Caravan Sites</div>
  <div class="tile-label" style="left:444px;top:673px">Places To Eat</div>
  <div class="tile-label" style="left:841px;top:673px">Cultural Sites</div>

  <section class="news-heading">
    <h2>NEWS FROM QUILLHAVEN</h2>
    <p>LATEST NEWS AND PROMOTIONS</p>
  </section>

  <div class="news-card" style="left:11px;width:268px;background:linear-gradient(180deg,#5593d8,#7aa8d6 55%,#8b9698)" role="img" aria-label="Castle ruins against a blue sky"></div>
  <div class="news-card" style="left:309px;width:265px;background:linear-gradient(180deg,#2c4a7a,#3a5d6e 50%,#9c9c88)" role="img" aria-label="Sandy bay with breaking waves"></div>
  <div class="news-card" style="left:608px;width:266px;background:linear-gradient(180deg,#1f3a78,#2c4680 55%,#5a4a38)" role="img" aria-label="Castle ruins at dusk"></div>
  <div class="news-card" style="left:905px;width:265px;background:linear-gradient(180deg,#2c4a7a,#3a5d6e 50%,#9c9c88)" role="img" aria-label="Sandy bay with breaking waves"></div>
</body>
</html>
```